Business Card Design for Fashion Tech Startup

Dear designers, we need a business card for Asia's premier fashion tech startup.!

PebbleHop is discovery e-commerce destination for busy, discerning parents in Asia featuring leading independent designers of baby, kids fashion apparel and sustainable brands from around the world.

PebbleHop is a modern, contemporary fashion tech startup targeting well-educated, well travelled and affluent parents. We're NOT your typical kiddy store!! Our design philosophy & e-commerce site is more like Vask.com, Orimesa.com, Pondwick.com, Farthollow.com.
Updates

Hi, size of the business card should be 84mm X 55mm. Would appreciate some business card layouts in Portrait as added consideration, i fancy the idea of a Portrait business card. What's important is that the business card should pique the receiver's interest to log onto the website to learn more. Many thanks and love forward to the designs!

Target Market(s)

Though modern, classy in look, feel & positioning, PebbleHop does possess a cheeky, fun-loving personality as depicted by its logo and the segment it targets (baby, kids) though the key decision makers i.e primarily mums between 25-40 who are well educated/travelled, local & expatriates, internet/digitally savvy, mid-high income working mums.

Industry/Entity Type

E-Commerce

Requirements
Must have
• Name, designation, email, phone & mobile number.
Company url : www.pebblehop.sg
Slogan : Discovery e-commerce destination for discerning, busy parents
Nice to have
• Call to Action such as a Discount code offering 10% discount
or asking people to "Like" us on our Chatterly page/Chatterly URL

```html
<!DOCTYPE html>
<html lang="en">
<head>
<meta charset="utf-8">
<title>PebbleHop Business Card</title>
<link rel="stylesheet" href="https://fonts.googleapis.com/css2?family=Open+Sans:wght@400;600;700&display=swap">
<style>
  :root {
    --page: #d9d6d2;
    --card: #2a2727;
    --slate: #3f6079;
    --slate-dark: #34506a;
    --salmon: #f27d6b;
    --salmon-deep: #e5705f;
    --band-fade: #6a5660;
    --text-light: #e7e3e0;
    --text-muted: #b9b3b0;
  }
  * { box-sizing: border-box; margin: 0; padding: 0; }
  html, body {
    width: 1200px; height: 919px; overflow: hidden;
    background: var(--page);
    font-family: "Open Sans", Arial, sans-serif;
  }
  .canvas { position: relative; width: 1200px; height: 919px; }

  .card {
    position: absolute;
    width: 560px; height: 367px;
    border-radius: 22px;
    background: var(--card);
    overflow: hidden;
    box-shadow: 0 10px 26px rgba(0,0,0,0.28);
  }
  .card--front { left: 60px; top: 60px; }
  .card--back  { left: 580px; top: 492px; }

  .edge { position: absolute; left: 0; right: 0; height: 18px; background: var(--slate); }
  .edge--top { top: 0; }
  .edge--bottom { bottom: 0; }
  .band {
    position: absolute; left: 0; right: 0; height: 30px;
    background: linear-gradient(90deg, var(--band-fade) 0%, var(--salmon) 28%, var(--salmon) 62%, var(--band-fade) 100%);
  }
  .band--top { top: 28px; }
  .band--bottom { bottom: 28px; }

  /* front */
  .mark-dot {
    position: absolute; left: 46px; top: 120px;
    width: 118px; height: 118px; border-radius: 50%;
    background: var(--slate);
  }
  .brand-name {
    position: absolute; color: var(--salmon); font-weight: 700; letter-spacing: 0.5px;
  }
  .card--front .brand-name { left: 150px; top: 66px; font-size: 38px; }
  .person { position: absolute; left: 218px; top: 124px; }
  .person-name { color: var(--salmon); font-size: 20px; font-weight: 600; letter-spacing: 1px; }
  .person-role { color: var(--text-muted); font-size: 14px; margin-top: 2px; }
  .contacts { position: absolute; left: 218px; top: 188px; list-style: none; }
  .contacts li {
    display: flex; align-items: center; gap: 9px;
    color: var(--text-light); font-size: 15px; line-height: 22px;
  }
  .contacts svg { width: 13px; height: 13px; flex: none; }

  /* back */
  .slogan {
    position: absolute; left: 40px; right: 30px; top: 66px;
    color: var(--slate); font-size: 17px; font-weight: 600; text-align: center;
  }
  .card--back .mark-dot { left: 70px; top: 124px; width: 122px; height: 122px; }
  .card--back .brand-name { left: 212px; top: 150px; font-size: 58px; }
  .cta {
    position: absolute; left: 40px; right: 30px; top: 272px;
    color: var(--slate); font-size: 16px; font-weight: 600; text-align: center;
  }
</style>
</head>
<body>
<main class="canvas">

  <section class="card card--front" aria-label="Business card front">
    <div class="edge edge--top"></div>
    <div class="band band--top"></div>
    <div class="mark-dot"></div>
    <div class="brand-name">PebbleHop</div>
    <div class="person">
      <p class="person-name">MARCUS LINDQVIST</p>
      <p class="person-role">Director</p>
    </div>
    <ul class="contacts">
      <li>
        <svg viewBox="0 0 14 14"><circle cx="7" cy="7" r="6.2" fill="none" stroke="#f27d6b" stroke-width="1.4"/><path d="M4.6 4.2l1.3-.2.7 1.6-.8.7c.4.9 1 1.5 1.9 1.9l.7-.8 1.6.7-.2 1.3c-2.9.2-5.4-2.3-5.2-5.2z" fill="#f27d6b"/></svg>
        0412555087
      </li>
      <li>
        <svg viewBox="0 0 14 14"><rect x="1" y="1" width="12" height="12" rx="2" fill="#f27d6b"/></svg>
        chatterly.com/
      </li>
      <li>
        <svg viewBox="0 0 14 14"><rect x="1" y="3" width="12" height="8" fill="#f27d6b"/><path d="M1 3l6 4.5L13 3" fill="none" stroke="#2a2727" stroke-width="1.2"/></svg>
        info@pebblehop.com
      </li>
      <li>
        <svg viewBox="0 0 14 14"><circle cx="7" cy="7" r="6" fill="#f27d6b"/><path d="M1 7h12M7 1c-2.6 3.4-2.6 8.6 0 12M7 1c2.6 3.4 2.6 8.6 0 12" fill="none" stroke="#2a2727" stroke-width="1"/></svg>
        www.pebblehop.asia
      </li>
    </ul>
    <div class="band band--bottom"></div>
    <div class="edge edge--bottom"></div>
  </section>

  <section class="card card--back" aria-label="Business card back">
    <div class="edge edge--top"></div>
    <div class="band band--top"></div>
    <p class="slogan">Discovery e-commerce destination for discerning, busy parents</p>
    <div class="mark-dot"></div>
    <div class="brand-name">PebbleHop</div>
    <p class="cta">Like us on our Chatterly page/Chatterly URL</p>
    <div class="band band--bottom"></div>
    <div class="edge edge--bottom"></div>
  </section>

</main>
</body>
</html>
```